Tarvolink - Smart Border Flow Reshaping Trade

Web Design for international start-up, which is automating customs clearance processes for forwarding companies by applying a web application, which is operating with artificial intelligence and robotic process automation. Tarvolink pursues the vision of supporting forwarding companies successfully in becoming digital masters and co-creates innovative software solutions with all participants (ex- and importers of goods) along value-added chains. With intelligent/smart/digital customs clearance software or in other words, a virtual customs clearance roboter tailord to the customers needs, we are transforming businesses. The website could look like this:

https://www.qorvanta.example/uk-en/index.php
or
https://pagelumen.example/theme/brindlemoor

Please use colours and designs you think would be the best fit. These websites are just here to give you an idea of how the webdesign could look like. Use the attached logo design as a basis for further web design. You can use the provided pictures, but you can also use your own ones, if you think they are better suited. But please take care, that they have a high resolution quality.

Description of Website: The website is transparent and modern. It provides seven pages such as homepage, products, web app, the about us, working at Tarvolink, News, contact us and search results page. The homepage or landing page should be filled with a short description of the company, what Tarvolink is doing, how they will support its customers and will also include a video of the provided solution. Products provide obviously information about different products and their characteristics. Web app page includes information about principles and technologies that get the software going. The about us page includes unique advantages and value propositions for customers and the contact us, as the name already says, will provide contact information and possibilities to contact us. The rest is also obvious (for additional information look up the website of QVT, priorly provided link - the page is also available in english).

If you have any questions, I am happy to answer them any time.
Updates

I have to think about the text that I want to have included into the design and hadn't have the time to compose it.

Target Market(s)

Forwarding Companies, Ex-/Importers

Industry/Entity Type

It Company

Number of Pages Required

5+ page

Requirements
Must have
• The web design should be designes according to the attached logo of Tarvolink.

```html
<!DOCTYPE html>
<html lang="en">
<head>
<meta charset="utf-8">
<title>Tarvolink – Smart Border Flow</title>
<link href="https://fonts.googleapis.com/css2?family=Cabin:wght@500;600;700&family=Roboto:wght@400;500;700&display=swap" rel="stylesheet">
<style>
:root{
  --cyan:#1ba9d8;
  --cyan-bright:#22b5e3;
  --indigo:#3f45a6;
  --indigo-deep:#363d98;
  --ink:#1d1d22;
  --text:#5d5f66;
  --muted:#8a8c93;
  --pale:#f4f6f9;
  --line:#d9e6ee;
  --white:#ffffff;
  --red:#e8262b;
}
*{box-sizing:border-box;margin:0;padding:0}
html,body{width:1200px;height:3333px;overflow:hidden}
body{position:relative;font-family:"Roboto",Arial,sans-serif;color:var(--text);background:var(--white)}
.abs{position:absolute}
.brand{font-family:"Cabin",Arial,sans-serif;font-weight:600;color:var(--white);line-height:1}
.brand-name{font-size:44px;letter-spacing:1px}
.brand-tag{font-size:12px;font-weight:500;display:block;text-align:right;margin-top:2px;font-family:"Roboto",Arial,sans-serif}

/* hero */
.hero{left:0;top:0;width:1200px;height:600px;background:linear-gradient(105deg,#23b0e0 0%,#2c95d2 40%,#3d5fb8 75%,#4a46a8 100%)}
.hero-wave{left:0;top:575px;width:1200px;height:40px}
.site-logo{left:142px;top:24px}
.main-nav{left:430px;top:44px;display:flex;gap:16px;align-items:center;font-family:"Roboto",Arial,sans-serif;font-weight:500;font-size:15.5px;color:var(--white)}
.hero-lead{left:300px;top:326px;width:600px;text-align:center;font-family:"Cabin",Arial,sans-serif;font-weight:700;font-size:20.5px;line-height:29px;color:var(--white)}

/* services */
.service{width:290px;height:296px;border-radius:50%;background:var(--white);text-align:center;
  box-shadow:0 9px 0 -1px var(--cyan),0 4px 18px rgba(20,40,90,.12)}
.service.is-active{background:var(--cyan);box-shadow:0 9px 0 -1px var(--indigo),0 4px 18px rgba(20,40,90,.15)}
.service svg{margin-top:58px}
.service h3{font-family:"Roboto",Arial,sans-serif;font-weight:500;font-size:23px;letter-spacing:3px;color:var(--ink);margin-top:12px}
.service p{font-size:13.5px;line-height:23px;color:var(--muted);width:210px;margin:12px auto 0}
.service.is-active h3,.service.is-active p{color:var(--white)}

/* welcome */
.ghost{font-family:"Cabin",Arial,sans-serif;font-weight:700;color:rgba(30,30,40,.07);white-space:nowrap}
.section-title{font-family:"Cabin",Arial,sans-serif;font-weight:700;color:var(--ink);letter-spacing:-.5px}
.centered{text-align:center;width:1200px;left:0}
.intro p{font-size:14px;line-height:24px;color:var(--text);text-align:center}
.video-band{left:0;top:1330px;width:1200px;height:342px;background:linear-gradient(180deg,#1da8da,#2a9ad6)}
.media{background:linear-gradient(135deg,#c6ccd2,#6f7780 55%,#3b424b)}
.play{width:60px;height:42px;border-radius:11px;background:var(--red)}
.play::after{content:"";position:absolute;left:24px;top:12px;border-left:16px solid #fff;border-top:9px solid transparent;border-bottom:9px solid transparent}

/* about */
.about{left:0;top:1671px;width:1200px;height:1296px;background:var(--pale)}
.side-word{left:-110px;top:1920px;transform:rotate(-90deg);font-family:"Cabin",Arial,sans-serif;font-weight:700;font-size:76px;color:rgba(30,30,40,.08);width:420px;text-align:center}
.about-copy p{font-size:14.5px;line-height:27px;color:var(--text);text-align:justify}
.btn{display:inline-block;background:var(--cyan);color:var(--white);font-family:"Roboto",Arial,sans-serif;font-weight:700;border-radius:30px}
.frame{left:723px;top:1797px;width:406px;height:261px;border:3px solid var(--cyan)}
.divider{left:144px;top:2254px;width:911px;height:1px;background:var(--line)}

/* news */
.news-card{width:284px}
.news-img{height:174px;border:3px solid var(--white);box-shadow:0 1px 4px rgba(0,0,0,.1)}
.date{left:14px;top:14px;width:52px;height:52px;border-radius:50%;background:var(--indigo);color:var(--white);text-align:center;line-height:1}
.date small{display:block;font-size:10.5px;margin-top:9px}
.date b{display:block;font-size:19px;font-weight:700;margin-top:2px}
.news-card h4{font-family:"Roboto",Arial,sans-serif;font-weight:400;font-size:18px;line-height:25px;color:#2c2d33;margin-top:22px}
.meta{font-size:14px;color:var(--muted);margin-top:10px;display:flex;align-items:center;gap:8px}
.news-card p{font-size:13.5px;line-height:22px;color:var(--muted);margin-top:10px;text-align:justify}
.read-more{display:inline-block;margin-top:18px;padding:8px 18px;border-radius:20px;background:var(--white);color:var(--cyan);font-weight:700;font-size:13.5px;box-shadow:0 1px 5px rgba(0,0,0,.12)}

/* footer */
.footer{left:0;top:2967px;width:1200px;height:366px;background:var(--indigo)}
.footer h5{font-family:"Roboto",Arial,sans-serif;font-weight:500;font-size:17px;color:var(--white)}
.footer li{list-style:none;font-size:13.5px;color:var(--white);height:27px;display:flex;align-items:center;gap:12px}
.social{width:34px;height:34px;border:1.5px solid var(--white);border-radius:50%}
.social::after{content:"";position:absolute;left:12px;top:12px;width:8px;height:8px;border-radius:50%;background:var(--white)}
.field{left:817px;top:3125px;width:237px;height:33px;border:1px solid rgba(255,255,255,.8);color:var(--white);font-size:11.5px;padding:9px 12px}
.footer-rule{left:400px;top:3256px;width:800px;height:1px;background:rgba(255,255,255,.25)}
.copyright{left:0;top:3286px;width:1200px;text-align:center;font-size:15px;color:var(--white)}
</style>
</head>
<body>

<!-- Hero -->
<div class="abs hero"></div>
<svg class="abs hero-wave" viewBox="0 0 1200 40" preserveAspectRatio="none" aria-hidden="true">
  <path d="M0 20 Q20 8 40 18 T80 16 T120 20 T160 14 T200 20 T240 16 T280 20 T320 14 T360 19 T400 15 T440 20 T480 14 T520 19 T560 16 T600 20 T640 15 T680 19 T720 14 T760 20 T800 16 T840 19 T880 14 T920 20 T960 16 T1000 19 T1040 14 T1080 20 T1120 15 T1160 19 T1200 16 V40 H0Z" fill="#ffffff"/>
</svg>

<div class="abs brand site-logo">
  <span class="brand-name">Tarvolink</span>
  <span class="brand-tag">Smart Border Flow</span>
</div>

<nav class="abs main-nav">
  <span>Home</span><span>Products</span><span>Web App</span><span>About Us</span><span>Working At Tarvolink</span><span>News</span><span>Contact Us</span>
  <svg width="16" height="16" viewBox="0 0 16 16" aria-hidden="true"><circle cx="6.5" cy="6.5" r="5" fill="none" stroke="#fff" stroke-width="2.2"/><path d="M10.5 10.5 L15 15" stroke="#fff" stroke-width="2.4" stroke-linecap="round"/></svg>
</nav>

<p class="abs hero-lead">Lorem ipsum dolor sit amet consectetur adipiscing elit sed do eiusmod tempor incididunt ut labore.</p>

<!-- Services -->
<div class="abs service" style="left:141px;top:511px">
  <svg width="100" height="62" viewBox="0 0 100 62" aria-hidden="true" fill="none" stroke="#3f45a6" stroke-width="3">
    <path d="M4 30 H50 V10 H74 L82 24 H96 V46 H4Z"/><path d="M58 14 H70 L76 24 H58Z"/><circle cx="24" cy="48" r="8" fill="#fff"/><circle cx="78" cy="48" r="8" fill="#fff"/><path d="M40 36 H50"/>
  </svg>
  <h3>PICKUP</h3>
  <p>Lorem ipsum dolor sit consectetur adipiscing elit do eiusmod tempor incididunt labore dolore</p>
</div>
<div class="abs service is-active" style="left:455px;top:511px">
  <svg width="70" height="66" viewBox="0 0 70 66" aria-hidden="true" fill="none" stroke="#fff" stroke-width="3">
    <rect x="20" y="4" width="38" height="56" rx="3"/><path d="M30 4 V0 H48 V4"/><path d="M30 16 H50 M34 24 H50 M40 44 H50 M40 50 H50"/><circle cx="24" cy="36" r="10"/><path d="M17 43 L6 56"/>
  </svg>
  <h3>CLEARANCE</h3>
  <p>Lorem ipsum dolor sit consectetur adipiscing elit do eiusmod tempor incididunt labore dolore</p>
</div>
<div class="abs service" style="left:769px;top:511px">
  <svg width="66" height="66" viewBox="0 0 66 66" aria-hidden="true" fill="none" stroke="#3f45a6" stroke-width="3">
    <path d="M2 14 V2 H14 M52 2 H64 V14 M64 52 V64 H52 M14 64 H2 V52"/><rect x="12" y="12" width="16" height="16"/><rect x="38" y="12" width="16" height="16"/><rect x="12" y="38" width="16" height="16"/><path d="M38 38 H46 V46 M54 38 V54 H42"/>
  </svg>
  <h3>PROTEST</h3>
  <p>Lorem ipsum dolor sit consectetur adipiscing elit do eiusmod tempor incididunt labore dolore</p>
</div>

<!-- Welcome -->
<div class="abs ghost centered" style="top:896px;font-size:76px;letter-spacing:1px">ABOUT TARVOLINK</div>
<h2 class="abs section-title centered" style="top:912px;font-size:44px">WELCOME TO TARVOLINK</h2>
<div class="abs intro" style="left:215px;top:999px;width:770px">
  <p>Lorem ipsum dolor sit amet, consectetur adipiscing elit, sed do eiusmod tempor incididunt ut labore et dolore magna aliqua.Ut enim ad minim veniam, quis nostrud exercitation ullamco laboris.</p>
  <p style="margin-top:14px">Nisi ut aliquip ex ea commodo consequat. Duis aute irure dolor in reprehenderit in voluptate velit esse cillum fugiat nulla pariatur. Excepteur sint occaecat cupidatat non proident, sunt in culpa qui officia deserunt mollit anim id est laborum.Sed ut perspiciatis unde omnis iste natus error sit voluptatem accusantium.</p>
</div>

<svg class="abs" style="left:0;top:1330px" width="1200" height="70" viewBox="0 0 1200 70" aria-hidden="true"><path d="M0 62 L1200 0 V70 H0Z" fill="#1da8da"/></svg>
<div class="abs video-band" style="top:1392px;height:280px"></div>
<div class="abs media" style="left:233px;top:1205px;width:734px;height:363px" role="img" aria-label="Video still: a customs agent with a headset working at a desk with computer screens"></div>
<div class="abs play" style="left:570px;top:1365px"></div>

<!-- About -->
<div class="abs about"></div>
<div class="abs side-word">ABOUT US</div>
<h2 class="abs section-title" style="left:144px;top:1790px;font-size:39px">WHAT TARVOLINK IS DOING</h2>
<div class="abs about-copy" style="left:144px;top:1862px;width:478px">
  <p>Lorem ipsum dolor sit amet, consectetur adipiscing elit, sed do eiusmod tempor incididunt ut labore et dolore magna aliqua.</p>
  <p style="margin-top:19px">Ut enim ad minim veniam, quis nostrud exercitation ullamco laboris nisi ut aliquip ex ea commodo consequat. Duis aute irure dolor in reprehenderit in voluptate velit esse cillum dolore eu fugiat nulla pariatur. Excepteur sint occaecat cupidatat non proident, sunt in culpa qui officia.</p>
</div>
<span class="abs btn" style="left:144px;top:2084px;width:169px;height:47px;line-height:47px;text-align:center;font-size:17px">READ MORE ➜</span>

<div class="abs frame"></div>
<div class="abs media" style="left:674px;top:1872px;width:390px;height:259px;background:linear-gradient(135deg,#e9ecef,#c9cfd6 55%,#9aa3ad)" role="img" aria-label="Video still: a team meeting around a table with sticky notes on the wall"></div>
<div class="abs play" style="left:840px;top:1981px;width:58px;height:40px"></div>
<div class="abs divider"></div>

<!-- News -->
<div class="abs ghost centered" style="top:2335px;font-size:76px">LATEST NEWS</div>
<h2 class="abs section-title centered" style="top:2354px;font-size:42px">LATEST NEWS</h2>
<p class="abs centered" style="top:2427px;font-size:13.5px;color:var(--text)">Lorem ipsum dolor sit amet, consectetur adipiscing elit, sed do eiusmod tempor incididunt</p>

<article class="abs news-card" style="left:142px;top:2480px">
  <div class="abs date" style="position:absolute;z-index:2"><small>Apr</small><b>12</b></div>
  <div class="news-img" style="background:linear-gradient(135deg,#8da2b4,#c56e4a 45%,#4c6a84)" role="img" aria-label="Aerial view of a container port"></div>
  <h4>Minus id quod maxime placeat Facere possimus</h4>
  <div class="meta"><span style="color:var(--indigo)">●</span> Ravenel &nbsp;|&nbsp; <span style="color:var(--indigo)">◆</span> 214 Comments</div>
  <p>Nam libero tempore, cum soluta nobis est eli gendi optio cumque nihil impedit.</p>
  <span class="read-more">Read More ➜</span>
</article>
<article class="abs news-card" style="left:457px;top:2480px">
  <div class="abs date" style="position:absolute;z-index:2;background:var(--cyan-bright)"><small>Apr</small><b>05</b></div>
  <div class="news-img" style="background:linear-gradient(135deg,#6f7a84,#2c3138 55%,#5a9ab8)" role="img" aria-label="Hands typing on a laptop keyboard"></div>
  <h4>Minus id quod maxime placeat Facere possimus</h4>
  <div class="meta"><span style="color:var(--indigo)">●</span> Ravenel &nbsp;|&nbsp; <span style="color:var(--indigo)">◆</span> 214 Comments</div>
  <p>Nam libero tempore, cum soluta nobis est eli gendi optio cumque nihil impedit.</p>
  <span class="read-more">Read More ➜</span>
</article>
<article class="abs news-card" style="left:772px;top:2480px">
  <div class="abs date" style="position:absolute;z-index:2"><small>Apr</small><b>22</b></div>
  <div class="news-img" style="background:linear-gradient(135deg,#8c8780,#d8d6d1 50%,#5d8fa0)" role="img" aria-label="Hands holding an open report with charts"></div>
  <h4>Minus id quod maxime placeat Facere possimus</h4>
  <div class="meta"><span style="color:var(--indigo)">●</span> Ravenel &nbsp;|&nbsp; <span style="color:var(--indigo)">◆</span> 214 Comments</div>
  <p>Nam libero tempore, cum soluta nobis est eli gendi optio cumque nihil impedit.</p>
  <span class="read-more">Read More ➜</span>
</article>

<!-- Footer -->
<footer class="abs footer"></footer>
<div class="abs brand" style="left:142px;top:3038px">
  <span class="brand-name" style="font-size:40px">Tarvolink</span>
  <span class="brand-tag" style="font-size:10px">Smart Border Flow</span>
</div>
<div class="abs social" style="left:158px;top:3115px"></div>
<div class="abs social" style="left:200px;top:3115px"></div>
<div class="abs social" style="left:243px;top:3115px"></div>
<div class="abs social" style="left:286px;top:3115px"></div>

<div class="abs footer" style="background:none;left:402px;top:3040px;width:160px;height:auto">
  <h5>QUICK LINKS</h5>
  <ul style="margin-top:17px">
    <li>» <span>Home</span></li><li>» <span>About Us</span></li><li>» <span>Services</span></li><li>» <span>Products</span></li><li>» <span>Contact Us</span></li>
  </ul>
</div>
<div class="abs footer" style="background:none;left:577px;top:3040px;width:220px;height:auto">
  <h5>CONTACT US</h5>
  <ul style="margin-top:17px">
    <li style="height:auto;align-items:flex-start;line-height:21px">
      <svg width="10" height="14" viewBox="0 0 10 14" aria-hidden="true" style="margin-top:4px"><path d="M5 0 A5 5 0 0 1 10 5 C10 8 5 14 5 14 C5 14 0 8 0 5 A5 5 0 0 1 5 0Z" fill="#fff"/><circle cx="5" cy="5" r="2" fill="#3f45a6"/></svg>
      <span>48 Larkmoor Row, Fennick City,<br>Brayle State</span></li>
    <li style="margin-top:12px">
      <svg width="12" height="12" viewBox="0 0 12 12" aria-hidden="true"><path d="M2 0 L4.5 3 L3 4.5 C4 6.5 5.5 8 7.5 9 L9 7.5 L12 10 L10 12 C5 11 1 7 0 2Z" fill="#fff"/></svg>
      <span>(+1) 555 014 2290</span></li>
    <li style="margin-top:16px">
      <svg width="14" height="10" viewBox="0 0 14 10" aria-hidden="true"><rect width="14" height="10" fill="#fff"/><path d="M0 0 L7 6 L14 0" fill="none" stroke="#3f45a6" stroke-width="1.4"/></svg>
      <span>support@tarvolink.example</span></li>
  </ul>
</div>
<div class="abs footer" style="background:none;left:817px;top:3040px;width:250px;height:auto">
  <h5>NEWSLETTER SUBSCRIPTION</h5>
  <p style="margin-top:18px;font-size:12.5px;line-height:17px;color:var(--white)">Register your Email Address to get more Information about us</p>
</div>
<div class="abs field">Email Address</div>
<span class="abs btn" style="left:817px;top:3173px;width:101px;height:33px;line-height:33px;text-align:center;font-size:11.5px">SUBSCRIBE</span>

<div class="abs footer-rule"></div>
<p class="abs copyright">Copyrights © 2019 Tarvolink.&nbsp; All Rights Reserved &nbsp;&nbsp; | &nbsp;&nbsp; Site Map</p>

</body>
</html>
```